Banner-Design für Verkauf von Organic und fair Trade Mode
Zielgruppe
Wir starten einen Internetshop mit dem Verkauf von Organic und fair Trade Mode. Mit eigenen Designs aber wir verkaufen auch die Ware ohne Design.
Ein Shirt Designer ist angeschlossen so dass die Kunden auch die Shirts selbst gestalten können.
1. Textildruck Service
2. Verkauf von bedruckten und unbedruckten Shirts
3. Kunden können jedes Kleidungsstück im Shop individualisieren
Aufgabenstellung
Wir benötigen 4 Banner für unseren Shop. Die Bilder sollen über die komplette breite der Startseite des Shops gehen. Plan ist es die Banner in einem Slider nach einander laufen zu lassen.
1. Banner der auf unseren Printservice auch für Firmen, Schulen, Vereine etc. hinweist
2.Jedes Shirt kann selbst gestaltet werden
3. Hinweisbanner auf Fair Trade und Organic Kategorien im Shop
4. Banner für anstehende SALE und permanente Mengenrabatt Aktionen
5. Drucktechniken
Größe: 1240 * 400 px and smaller like 900 * ~ 400px.
Als Dateien sind das Firmenlogo sowie das Logo unsers Labels beigefügt außerdem ist ein Banner der jedoch nicht professionell genug ist angehängt.
Farbgebung des Shops: Header und navigation schwarz / grau,
Daher sind wir für alle Vorschläge offen und würden die Zusammenarbeit gerne weiter ausbauen da wir dringend Grafiker / Designer benötigen.

```html
<!DOCTYPE html>
<html lang="de">
<head>
<meta charset="utf-8">
<title>Shop-Banner Serie</title>
<link href="https://fonts.googleapis.com/css2?family=Open+Sans:wght@400;700&display=swap" rel="stylesheet">
<style>
  :root {
    --page-bg: #2f2f2f;
    --box-bg: #2f2f2f;
    --text-light: #ffffff;
    --text-dark: #2f2f2f;
    --accent-red: #e8463a;
    --sky-light: #eef2f7;
    --sky-blue: #1d74c0;
    --forest-dark: #1e2b24;
    --forest-mid: #3b4a3a;
  }
  * { margin: 0; padding: 0; box-sizing: border-box; }
  html, body { width: 1200px; height: 862px; overflow: hidden; background: var(--page-bg); }
  body { position: relative; font-family: "Open Sans", sans-serif; }

  .banner { position: absolute; left: 323px; width: 554px; height: 179px; overflow: hidden; }
  .banner--print { top: 47px; }
  .banner--design { top: 243px; background: #ffffff; }
  .banner--organic { top: 440px; }
  .banner--sale { top: 637px; }

  .banner__photo { position: absolute; inset: 0; }
  .banner--print .banner__photo { background: linear-gradient(100deg, var(--sky-light) 0%, #e7ecf2 45%, #6fa4d4 62%, var(--sky-blue) 80%, #0f4f8f 100%); }
  .banner--design .banner__photo { left: 285px; background: linear-gradient(90deg, #ffffff 0%, #2a82c9 35%, #a1202a 65%, #ffffff 100%); }
  .banner--organic .banner__photo { background: linear-gradient(90deg, var(--forest-dark) 0%, var(--forest-mid) 55%, #6b2a30 75%, #33402f 100%); }
  .banner--sale .banner__photo { background: linear-gradient(180deg, #d9d9d9 0%, #f2f2f2 12%, #1d1d1d 28%, #d8261f 38%, #2a2a9a 52%, #1c5fc0 62%, #1a1a1a 70%, #f26a1b 82%, #e6e6e6 100%); }

  .pitch {
    position: absolute; left: 22px; top: 22px; width: 255px;
    background: var(--box-bg); color: var(--text-light);
    padding: 0 15px; display: flex; flex-direction: column; justify-content: center;
    font-size: 16px; line-height: 19.4px; text-transform: uppercase;
  }
  .banner--print .pitch, .banner--design .pitch { height: 94px; }
  .banner--organic .pitch { height: 74px; }
  .banner--sale .pitch { height: 114px; }
  .pitch strong { font-weight: 700; }
  .pitch .pitch__accent { color: var(--accent-red); font-weight: 700; }

  .brand {
    position: absolute; left: 36px; top: 133px;
    display: flex; align-items: center; gap: 5px;
    font-size: 11px; font-weight: 700; letter-spacing: 0.5px; text-transform: uppercase;
  }
  .brand__dot { width: 9px; height: 9px; border-radius: 50%; background: currentColor; }
  .brand--dark { color: var(--text-dark); }
  .brand--light { color: var(--text-light); }
  .banner--sale .brand { top: 140px; }

  .product-spot { position: absolute; top: 81px; width: 78px; height: 78px; border-radius: 50%; border: 2px solid #d8d8d8; }
  .product-spot--a { left: 388px; }
  .product-spot--b { left: 455px; }
  .banner--print .product-spot--a { background: #f4f4f4; }
  .banner--print .product-spot--b { background: #1a1a1a; }
  .banner--organic .product-spot--a { background: #f4f4f4; }
  .banner--organic .product-spot--b { background: #e23d93; }
</style>
</head>
<body>

<section class="banner banner--print">
  <div class="banner__photo" role="img" aria-label="Glasfassade eines Hochhauses vor hellem Himmel"></div>
  <div class="pitch">
    <span>Unser Printservice für</span>
    <strong>Unternehmen, Schulen,</strong>
    <strong>Vereine und mehr.</strong>
  </div>
  <div class="brand brand--dark"><span class="brand__dot"></span>Faserhaus</div>
  <div class="product-spot product-spot--a" role="img" aria-label="Weißes Shirt mit buntem Motiv"></div>
  <div class="product-spot product-spot--b" role="img" aria-label="Schwarzes Shirt mit rotem Herzmotiv"></div>
</section>

<section class="banner banner--design">
  <div class="banner__photo" role="img" aria-label="Zwei Models in blauem und rotem bedrucktem Shirt"></div>
  <div class="pitch">
    <span>Gestalten Sie</span>
    <strong>jedes Shirt</strong>
    <strong>nach Ihrem Geschmack.</strong>
  </div>
  <div class="brand brand--dark"><span class="brand__dot"></span>Faserhaus</div>
</section>

<section class="banner banner--organic">
  <div class="banner__photo" role="img" aria-label="Person mit kariertem Hemd im Wald"></div>
  <div class="pitch">
    <span>Organic &amp; Fair Trade –</span>
    <strong>hier im Shop.</strong>
  </div>
  <div class="brand brand--light"><span class="brand__dot"></span>Faserhaus</div>
  <div class="product-spot product-spot--a" role="img" aria-label="Weißes Shirt mit Elefantenmotiv"></div>
  <div class="product-spot product-spot--b" role="img" aria-label="Pinkes Shirt mit Baummotiv"></div>
</section>

<section class="banner banner--sale">
  <div class="banner__photo" role="img" aria-label="Gestapelte bunte Shirts"></div>
  <div class="pitch">
    <span>Verpassen Sie nicht</span>
    <span>die anstehenden</span>
    <span class="pitch__accent">Sale und Megarabatt</span>
    <strong>Aktionen.</strong>
  </div>
  <div class="brand brand--light"><span class="brand__dot"></span>Faserhaus</div>
</section>

</body>
</html>
```